Design a helpdesk ticketing platform *

We are launching a helpdesk ticketing platform. Very much like quellbox.com, merrylark.com, pivolta.com, brisktray.com etc. We have a full mid-fidelity prototype built and we want someone to build the full fidelity of the product.

You can view the full mid-fidelity prototype here: https://lnk.vexora.net/Qa8Lpw

The best way moving forward is to just design the following 4 pages

- Main Dashboard https://lnk.vexora.net/81hRtd
- All tickets https://lnk.vexora.net/jwNoEb
- Viewing a ticket https://lnk.vexora.net/Ys4VmK
- Contacts https://lnk.vexora.net/pHeXuo

Target Market(s)

Small business owners

Industry/Entity Type

Saas

Number of Pages Required

4 page

Font styles to use
Serif
Sans Serif

Colors

Designer to choose colors to be used in the design.

Requirements
Must have
• Must follow the prototype exactly. We are not looking for any UX changes. We want the designe xactly as the prototype is. We are only looking for design ideas.
Should not have
• modern, clean. We'd love to see the primary color as yellow, purple, orange, green or blue. You choose which one you think looks best and go with that.

```html
<!DOCTYPE html>
<html lang="en">
<head>
<meta charset="utf-8">
<title>DeskHarbor – All Tickets</title>
<link href="https://fonts.googleapis.com/css2?family=Roboto:wght@400;500;700&display=swap" rel="stylesheet">
<style>
:root{
  --navy:#213d8c;
  --navy-dark:#1c3577;
  --navy-row:#27509e;
  --navy-icon:#2a559f;
  --active:#3498db;
  --green:#27a869;
  --orange:#f5741d;
  --page:#e9ebf0;
  --panel:#ffffff;
  --line:#d7d9de;
  --text:#333;
  --muted:#555;
  --link:#2b4a8c;
  --footer:#1c1c1c;
}
*{box-sizing:border-box;margin:0;padding:0}
html,body{width:1200px;height:882px;overflow:hidden}
body{font-family:'Roboto',sans-serif;background:var(--page);color:var(--text);position:relative}
.abs{position:absolute}

/* sidebar */
.sidebar{left:0;top:0;width:197px;height:824px;background:var(--navy)}
.brand{left:0;top:0;width:197px;height:78px;background:var(--navy-dark);display:flex;align-items:center;padding-left:34px;gap:18px}
.brand-name{color:#fff;font-weight:700;font-size:22px;letter-spacing:-.3px}
.new-ticket{left:36px;top:102px;width:110px;height:30px;background:var(--green);border-radius:3px;color:#fff;font-size:13px;display:flex;align-items:center;padding-left:16px}
.new-ticket .dots{position:absolute;right:10px;top:8px}
.nav-item{left:0;width:197px;display:flex;align-items:center;color:#fff;font-size:14px;background:var(--navy-row);border-bottom:1px solid var(--navy-dark)}
.nav-item .ico{width:54px;height:100%;display:flex;align-items:center;justify-content:center;background:var(--navy-icon)}
.nav-item .label{padding-left:12px;flex:1}
.nav-item .caret{margin-right:16px}
.submenu{left:0;top:247px;width:197px}
.submenu div{height:25.4px;padding-left:65px;font-size:9.5px;color:#fff;display:flex;align-items:center}
.submenu .on{background:var(--active);height:28px}

/* header */
.page-title{left:233px;top:24px;font-size:22px;color:#444;font-weight:500}
.search{left:905px;top:20px;width:178px;height:34px;border:1px solid #555;border-radius:17px;display:flex;align-items:center;justify-content:space-between;padding:0 14px;font-size:11.5px;color:#333}
.avatar-me{left:1097px;top:15px;width:46px;height:46px;border-radius:50%;background:var(--navy-dark);color:#fff;font-size:19px;display:flex;align-items:center;justify-content:center}

/* filter panel */
.filter{left:197px;top:92px;width:245px;height:661px;background:var(--panel);border:1px solid var(--line)}
.filter-head{left:205px;top:102px;width:232px;height:24px;display:flex;align-items:center;font-size:13.5px}
.filter-head .title{margin-left:10px;margin-right:auto;display:flex;align-items:center;gap:6px}
.filter-head .discard{font-size:10.5px;color:#555;margin-right:10px}
.filter-head .save{background:var(--orange);color:#fff;font-size:10.5px;padding:4px 5px;border-radius:2px}
.f-label{left:226px;font-size:12px;color:#333}
.f-select{left:226px;width:193px;height:26px;border:1px solid #999;font-size:11px;color:#444;display:flex;align-items:center;padding-left:7px}
.f-select::after{content:"";position:absolute;right:8px;top:10px;border:4px solid transparent;border-top:5px solid #222}

/* tickets panel */
.tickets{left:450px;top:92px;width:696px;height:661px;background:var(--panel);border:1px solid var(--line)}
.tickets-head{left:450px;top:92px;width:696px;height:36px;background:#f0f0f2;display:flex;align-items:center;padding-left:27px;font-size:14px;color:#333}
.box{width:12px;height:12px;border:1.5px solid #777;border-radius:1px;display:inline-block}
.tickets-head .box{width:14px;height:14px;margin-right:10px}
.pager{position:absolute;right:16px;font-size:11.5px;color:#444;display:flex;align-items:center;gap:8px}
.table{left:465px;top:142px;width:667px;height:589px;border:1px solid #c8c8cc}
.col-check{left:465px;top:142px;width:35px;height:589px;border-right:1px solid #c8c8cc}
.hrule{left:465px;width:667px;height:1px;background:#c8c8cc}
.th{top:159px;font-size:12px;color:var(--link)}
.cell{font-size:11.5px;color:#333;display:flex;align-items:center;gap:4px}
.row-box{left:475px}
.avatar{left:507px;width:26px;height:26px;border-radius:50%;color:#fff;font-size:10.5px;display:flex;align-items:center;justify-content:center}

/* footer */
.footer{left:0;top:824px;width:1200px;height:58px;background:var(--footer);color:#fff;font-size:10px;display:flex;align-items:center;justify-content:center}
</style>
</head>
<body>

<aside class="abs sidebar"></aside>
<div class="abs brand">
  <span class="brand-name">DeskHarbor</span>
  <svg width="18" height="16" viewBox="0 0 18 16"><rect y="1" width="18" height="2.4" fill="#fff"/><rect y="7" width="18" height="2.4" fill="#fff"/><rect y="13" width="18" height="2.4" fill="#fff"/></svg>
</div>
<div class="abs new-ticket">New Ticket
  <svg class="dots" width="4" height="14" viewBox="0 0 4 14"><circle cx="2" cy="2" r="1.5" fill="#fff"/><circle cx="2" cy="7" r="1.5" fill="#fff"/><circle cx="2" cy="12" r="1.5" fill="#fff"/></svg>
</div>

<div class="abs nav-item" style="top:154px;height:46px">
  <span class="ico"><svg width="18" height="14" viewBox="0 0 18 14"><path d="M1 13a8 8 0 1 1 16 0z" fill="#fff"/><path d="M9 12l3-6" stroke="var(--navy-icon)" stroke-width="2"/></svg></span>
  <span class="label">Dashboard</span>
</div>
<div class="abs nav-item" style="top:200px;height:47px;background:#2c5ca8">
  <span class="ico" style="background:#2c5ca8"><svg width="18" height="12" viewBox="0 0 18 12"><rect x="1" y="1" width="16" height="10" rx="1.5" fill="none" stroke="#fff" stroke-width="2"/><rect x="5" y="4" width="8" height="4" fill="#fff"/></svg></span>
  <span class="label">Ticket</span>
  <svg class="caret" width="10" height="6" viewBox="0 0 10 6"><path d="M0 0h10L5 6z" fill="#fff"/></svg>
</div>
<nav class="abs submenu">
  <div class="on">All Tickets</div>
  <div>My Tickets</div>
  <div>Open Tickets</div>
  <div>Unassigned Tickets</div>
  <div>Spam</div>
  <div>Trash</div>
</nav>
<div class="abs nav-item" style="top:404px;height:46px">
  <span class="ico"><svg width="16" height="15" viewBox="0 0 16 15"><rect x="1" y="3" width="11" height="11" fill="none" stroke="#fff" stroke-width="1.6"/><path d="M6 9l8-8" stroke="#fff" stroke-width="2"/></svg></span>
  <span class="label">Contacts</span>
</div>
<div class="abs nav-item" style="top:450px;height:47px">
  <span class="ico"><svg width="16" height="16" viewBox="0 0 16 16"><circle cx="8" cy="8" r="5" fill="none" stroke="#fff" stroke-width="3.5" stroke-dasharray="2.6 1.3"/><circle cx="8" cy="8" r="3.6" fill="#fff"/><circle cx="8" cy="8" r="1.6" fill="var(--navy-icon)"/></svg></span>
  <span class="label">Admin Setting</span>
  <svg class="caret" width="10" height="6" viewBox="0 0 10 6"><path d="M0 0h10L5 6z" fill="#fff"/></svg>
</div>
<div class="abs nav-item" style="top:497px;height:46px">
  <span class="ico"><svg width="13" height="16" viewBox="0 0 13 16"><path d="M0 0h9l4 4v12H0z" fill="#fff"/><path d="M3 8h7M3 11h7" stroke="var(--navy-icon)" stroke-width="1.2"/></svg></span>
  <span class="label">Account &amp; Billing</span>
</div>

<h1 class="abs page-title">Tickets &gt; All Tickets</h1>
<div class="abs search">Search
  <svg width="12" height="12" viewBox="0 0 12 12"><circle cx="5" cy="5" r="3.6" fill="none" stroke="#222" stroke-width="1.8"/><path d="M7.6 7.6L11 11" stroke="#222" stroke-width="2"/></svg>
</div>
<div class="abs avatar-me">AK</div>

<section class="abs filter"></section>
<div class="abs filter-head">
  <svg width="6" height="9" viewBox="0 0 6 9"><path d="M6 0v9L0 4.5z" fill="#333"/></svg>
  <span class="title"><svg width="14" height="12" viewBox="0 0 14 12"><path d="M0 2h14M0 6h14M0 10h14" stroke="#333" stroke-width="1.4"/><rect x="8" y="0.5" width="2" height="3" fill="#333"/><rect x="3" y="4.5" width="2" height="3" fill="#333"/><rect x="6" y="8.5" width="2" height="3" fill="#333"/></svg>Filter</span>
  <span class="discard">Discard</span>
  <span class="save">Save Filter as</span>
</div>

<div class="abs f-label" style="top:151px">Agents</div><div class="abs f-select" style="top:172px">Steven</div>
<div class="abs f-label" style="top:215px">Groups</div><div class="abs f-select" style="top:236px">Any</div>
<div class="abs f-label" style="top:279px">Created</div><div class="abs f-select" style="top:300px">Any</div>
<div class="abs f-label" style="top:344px">Status</div><div class="abs f-select" style="top:365px">Any</div>
<div class="abs f-label" style="top:410px">Priorty</div><div class="abs f-select" style="top:431px">Low</div>
<div class="abs f-label" style="top:475px">Source</div><div class="abs f-select" style="top:496px">Any</div>
<div class="abs f-label" style="top:539px">Tags</div><div class="abs f-select" style="top:560px">Any</div>
<div class="abs f-label" style="top:605px">Companies</div><div class="abs f-select" style="top:626px">Low</div>
<div class="abs f-label" style="top:669px">Contacts</div><div class="abs f-select" style="top:690px">Any</div>

<section class="abs tickets"></section>
<div class="abs tickets-head"><span class="box"></span>Select All
  <span class="pager">1-25 of 10 <svg width="6" height="10" viewBox="0 0 6 10"><path d="M5 1L1 5l4 4" fill="none" stroke="#333" stroke-width="1.8"/></svg></span>
</div>

<div class="abs table"></div>
<div class="abs col-check"></div>
<div class="abs hrule" style="top:188px"></div>
<div class="abs hrule" style="top:234px"></div>
<div class="abs hrule" style="top:284px"></div>
<div class="abs hrule" style="top:331px"></div>

<div class="abs th" style="left:510px">Contact</div>
<div class="abs th" style="left:655px">Subject</div>
<div class="abs th" style="left:817px">State</div>
<div class="abs th" style="left:902px">Group</div>
<div class="abs th" style="left:978px">Agent</div>
<div class="abs th" style="left:1066px">Priority</div>

<!-- row 1 -->
<span class="abs box row-box" style="top:204px"></span>
<div class="abs avatar" style="top:198px;background:#16a085">LT</div>
<div class="abs cell" style="left:541px;top:204px">Lily Thompson</div>
<div class="abs cell" style="left:654px;top:204px">I can't reset(#10)
  <svg width="32" height="12" viewBox="0 0 32 12"><path d="M5 6q7-7 14 0q-7 7-14 0z" fill="#666"/><circle cx="12" cy="6" r="2" fill="#fff"/><path d="M23 11l1-3 6-6 2 2-6 6z" fill="#666"/></svg></div>
<div class="abs cell" style="left:817px;top:204px">Past Due</div>
<div class="abs cell" style="left:902px;top:204px">Sales <svg width="7" height="4"><path d="M0 0h7L3.5 4z" fill="#333"/></svg></div>
<div class="abs cell" style="left:980px;top:204px">Andrew <svg width="7" height="4"><path d="M0 0h7L3.5 4z" fill="#333"/></svg></div>
<div class="abs cell" style="left:1070px;top:204px">Low</div>

<!-- row 2 -->
<span class="abs box row-box" style="top:254px"></span>
<div class="abs avatar" style="top:248px;background:#2a7fc4">MK</div>
<div class="abs cell" style="left:541px;top:255px">Lily Thompson</div>
<div class="abs cell" style="left:654px;top:255px">I can't reset(#10)
  <svg width="32" height="12" viewBox="0 0 32 12"><path d="M5 6q7-7 14 0q-7 7-14 0z" fill="#666"/><circle cx="12" cy="6" r="2" fill="#fff"/><path d="M23 11l1-3 6-6 2 2-6 6z" fill="#666"/></svg></div>
<div class="abs cell" style="left:817px;top:255px">Past Due</div>
<div class="abs cell" style="left:902px;top:255px">Sales <svg width="7" height="4"><path d="M0 0h7L3.5 4z" fill="#333"/></svg></div>
<div class="abs cell" style="left:980px;top:255px">Andrew <svg width="7" height="4"><path d="M0 0h7L3.5 4z" fill="#333"/></svg></div>
<div class="abs cell" style="left:1070px;top:255px">Low</div>

<!-- row 3 -->
<span class="abs box row-box" style="top:301px"></span>
<div class="abs avatar" style="top:295px;background:#3a9ee0">JS</div>
<div class="abs cell" style="left:541px;top:301px">Lily Thompson</div>
<div class="abs cell" style="left:654px;top:301px">I can't reset(#10)
  <svg width="32" height="12" viewBox="0 0 32 12"><path d="M5 6q7-7 14 0q-7 7-14 0z" fill="#666"/><circle cx="12" cy="6" r="2" fill="#fff"/><path d="M23 11l1-3 6-6 2 2-6 6z" fill="#666"/></svg></div>
<div class="abs cell" style="left:817px;top:301px">Past Due</div>
<div class="abs cell" style="left:902px;top:301px">Sales <svg width="7" height="4"><path d="M0 0h7L3.5 4z" fill="#333"/></svg></div>
<div class="abs cell" style="left:980px;top:301px">Andrew <svg width="7" height="4"><path d="M0 0h7L3.5 4z" fill="#333"/></svg></div>
<div class="abs cell" style="left:1070px;top:301px">Low</div>

<footer class="abs footer">Copyright © 2018. All Rights Reserved - Privacy Policy</footer>

</body>
</html>
```